Wordpress Theme for a Professional Speaker's Website

I I need a website to promote myself as a speaker to corporations and meeting planners. Some examples of similar sites I like are:

http://www.beginwithpurpose.example (this is by far my favorite)
http://www.tovaruskin.example
http://www.glenbeckworth.example
http://www.lomtrisel.example
http://www.dawnafterstorms.example
http://www.osricpellandine.example

I like modern, minimalistic, innovative. I'm okay if it's edgy but still want it communicate professionalism.

The primary objective is to position me as an expert who can deliver valuable information in an entertaining manner.

There are two calls to action. The first is to capture name and email address to subscribe to my newsletter. The second is to request more information about booking me to speak for their company, organization, etc.

The pages on the website will ultimately be the following:

1. Home (should include sections for recent blog posts, featured topics/presentations, short bio, testimonials, email capture, and anything else you think should be added.
2. Meet Ross
3. Blog
4. Keynotes & Speaking
5. Training & Webinars
6. Coaching & Consulting
7. Testimonials
8. Book Ross
9. Media Inquiries
10. Contact

Please feel free to use your creativity. I don't want my requirements to limit you in any way. I'm just looking for a modern, professional site that will make me stand out from the crowd.

I don't have any existing site or brand identity. My plan is to have the website design I ultimately choose serve as the foundation for the rest of my brand identity.

Target Market(s)

Corporate meeting planners and executives

Industry/Entity Type

It Professional

Font styles to use
Sans Serif

Requirements
Must have
• Email capture, testimonials, blog
Nice to have
• None
Should not have
• None

```html
<!DOCTYPE html>
<html lang="en">
<head>
<meta charset="utf-8">
<title>Ross Valdane — Speaker</title>
<link rel="stylesheet" href="https://fonts.googleapis.com/css2?family=Open+Sans:ital,wght@0,400;0,600;0,700;0,800;1,400&display=swap">
<style>
:root{
  --orange:#e0503a;
  --orange-dark:#c9412d;
  --ink:#333333;
  --charcoal:#2e2e2e;
  --black:#0b0b0b;
  --grey-light:#efefef;
  --grey-band:#f3f3f3;
  --text:#666666;
  --white:#ffffff;
  --line:#dddddd;
}
*{box-sizing:border-box;margin:0;padding:0}
html,body{width:1200px;height:3482px;overflow:hidden}
body{font-family:"Open Sans",Arial,sans-serif;color:var(--ink);background:var(--white);position:relative}
.abs{position:absolute}
section,header,footer{position:absolute;left:0;width:1200px}
p{font-size:11px;line-height:18px;color:var(--text)}

/* header */
.site-header{top:0;height:132px;background:var(--white);box-shadow:0 1px 0 #e6e6e6}
.utility-bar{right:0;top:0;width:666px;height:42px;background:var(--orange);clip-path:polygon(22px 0,100% 0,100% 100%,0 100%)}
.utility-bar a,.main-nav a{position:absolute;text-decoration:none;font-weight:600;font-size:11.5px;white-space:nowrap}
.utility-bar a{color:var(--white);top:13px}
.brand{left:162px;top:30px;font-weight:800;font-size:31px;line-height:31px;color:var(--ink);letter-spacing:.5px}
.main-nav a{top:86px;color:var(--ink);font-size:11.5px}
.main-nav a.active{color:var(--orange)}
.main-nav .marker{left:402px;top:124px;width:0;height:0;border-left:8px solid transparent;border-right:8px solid transparent;border-bottom:8px solid var(--orange)}

/* hero */
.hero{top:132px;height:534px;background:var(--black)}
.hero-photo{left:0;top:0;width:700px;height:534px;background:radial-gradient(ellipse at 42% 45%,#5a5048 0%,#2a2522 38%,#0b0b0b 75%)}
.hero-title{left:587px;top:190px;font-weight:800;color:var(--white);font-size:50px;line-height:56px;letter-spacing:.5px}
.hero-title span{display:block;color:#3f3f3f;font-size:80px;line-height:86px;letter-spacing:0}
.hero-dots{left:982px;top:466px;display:flex;gap:6px}
.hero-dots i{width:12px;height:12px;border-radius:50%;background:#555}
.hero-dots i.on{background:var(--orange)}

/* subscribe */
.subscribe{top:666px;height:88px;background:var(--charcoal)}
.subscribe-accent{left:430px;top:0;width:770px;height:88px;background:var(--orange);clip-path:polygon(40px 0,100% 0,100% 100%,0 100%)}
.subscribe h3{left:162px;top:23px;color:var(--white);font-size:14px;line-height:21px;font-weight:700}
.field{background:var(--white);border:1px solid #d8d8d8;font-size:10px;font-style:italic;color:#888;padding:0 10px;display:flex;align-items:center}
.btn-dark{background:var(--charcoal);color:var(--white);font-weight:700;font-size:11.5px;display:flex;align-items:center;justify-content:center}

/* seen on */
.seen-on{top:754px;height:70px;background:var(--grey-band)}
.seen-on .label{left:162px;top:27px;font-size:11px;font-weight:600;color:var(--ink)}
.partner-badge{top:20px;height:30px;background:#c9c9c9;border-radius:3px}

/* headings */
.section-title{width:1200px;left:0;text-align:center;font-weight:700;font-size:24px;color:var(--ink)}

/* topics */
.thumb{background:linear-gradient(135deg,#8a5a3c,#3b2a22)}
.card-title{font-weight:700;font-size:14px;color:var(--orange)}
.card-text{font-size:10.5px;line-height:16px;color:var(--text)}
.play{width:42px;height:42px;border:2px solid var(--white);border-radius:50%;display:flex;align-items:center;justify-content:center}

/* about */
.about{top:1400px;height:450px;background:var(--grey-light)}
.btn-orange{background:var(--orange);color:var(--white);font-weight:700;font-size:11px;display:flex;align-items:center;justify-content:center}
.btn-outline{border:2px solid #555;color:var(--ink);font-weight:700;font-size:11px;display:flex;align-items:center;justify-content:center;gap:8px}

/* testimonials */
.testimonials{top:1850px;height:360px;background:linear-gradient(180deg,#3a3a3a,#262626)}
.quote{left:343px;top:2020px;width:612px;color:#e6e6e6;font-style:italic;font-size:11.5px;line-height:21px}

/* blog */
.meta{display:flex;gap:18px;font-size:9.5px;font-weight:600;color:var(--ink);align-items:center}
.meta span{display:flex;align-items:center;gap:5px}

/* booking */
.booking{top:2616px;height:290px;background:linear-gradient(135deg,#e45a43,#d8452f)}
.booking .field{font-size:10px}
.booking .select{justify-content:space-between}

/* footer */
.site-footer{top:3250px;height:232px;background:var(--charcoal)}
.footer-nav a{position:absolute;color:var(--white);font-size:11px;font-weight:600;text-decoration:none;white-space:nowrap}
.social{width:28px;height:28px;border-radius:50%;background:#3a8ccf}
</style>
</head>
<body>

<header class="site-header">
  <nav class="utility-bar abs" aria-label="Secondary">
    <a style="left:35px">BLOG</a>
    <a style="left:93px">TESTIMONIALS</a>
    <a style="left:213px">BOOK ROSS</a>
    <a style="left:318px">MEDIA INQUIRIES</a>
    <a style="left:450px">CONTACT</a>
  </nav>
  <div class="brand abs">ROSS<br>VALDANE</div>
  <nav class="main-nav" aria-label="Main">
    <a class="active" style="left:390px">HOME</a>
    <a style="left:457px">MEET ROSS</a>
    <a style="left:583px">KEYNOTES &amp; SPEAKING</a>
    <a style="left:729px">TRAINING &amp; WEBINARS</a>
    <a style="left:882px">COACHING &amp; CONSULTING</a>
    <span class="marker abs"></span>
  </nav>
</header>

<section class="hero">
  <div class="hero-photo abs" role="img" aria-label="Speaker on stage in a grey suit gesturing to the audience, warm stage lights behind"></div>
  <h1 class="hero-title abs">BUILD A BETTER<span>BUSINESS</span></h1>
  <div class="hero-dots abs"><i></i><i></i><i class="on"></i><i class="on"></i></div>
</section>

<section class="subscribe">
  <div class="subscribe-accent abs"></div>
  <h3 class="abs">SUBSCRIBE AN EMAIL ADDRESS GET<br>YOUR BUSINESS SECRETS</h3>
  <div class="field abs" style="left:485px;top:23px;width:214px;height:42px">Name</div>
  <div class="field abs" style="left:708px;top:23px;width:211px;height:42px">Email address</div>
  <div class="btn-dark abs" style="left:928px;top:23px;width:110px;height:42px">SUBSCRIBE</div>
</section>

<section class="seen-on">
  <span class="label abs">AS SEEN ON :</span>
  <span class="partner-badge abs" style="left:298px;width:88px"></span>
  <span class="partner-badge abs" style="left:434px;width:50px"></span>
  <span class="partner-badge abs" style="left:549px;width:56px"></span>
  <span class="partner-badge abs" style="left:663px;width:30px"></span>
  <span class="partner-badge abs" style="left:783px;width:70px"></span>
  <span class="partner-badge abs" style="left:943px;width:82px"></span>
</section>

<section class="featured-topics" style="top:824px;height:576px">
  <h2 class="section-title abs" style="top:44px">FEATURED TOPICS/PRESENTATIONS</h2>
</section>
<!-- topic cards -->
<div class="thumb abs" style="left:162px;top:928px;width:177px;height:121px" role="img" aria-label="Audience seated at a conference"></div>
<div class="thumb abs" style="left:360px;top:928px;width:176px;height:121px;display:flex;align-items:center;justify-content:center" role="img" aria-label="Presenter at a projected screen, video">
  <span class="play"><svg width="14" height="16"><path d="M2 1 L13 8 L2 15Z" fill="#fff"/></svg></span></div>
<div class="thumb abs" style="left:559px;top:928px;width:177px;height:121px" role="img" aria-label="Hands writing notes in a workshop"></div>
<div class="thumb abs" style="left:162px;top:1147px;width:177px;height:120px;background:linear-gradient(135deg,#d9dde2,#8d97a3)" role="img" aria-label="Trainer at a whiteboard with colleagues"></div>
<div class="thumb abs" style="left:360px;top:1147px;width:176px;height:120px;background:linear-gradient(135deg,#c9ced4,#6b6560)" role="img" aria-label="Small team meeting in an office"></div>
<div class="thumb abs" style="left:559px;top:1147px;width:177px;height:120px;background:linear-gradient(135deg,#e4e4e4,#9a8d84)" role="img" aria-label="Participant listening in a seminar"></div>

<h4 class="card-title abs" style="left:162px;top:1058px">Finibus Bonorum</h4>
<h4 class="card-title abs" style="left:360px;top:1058px">Finibus Bonorum</h4>
<h4 class="card-title abs" style="left:559px;top:1058px">Finibus Bonorum</h4>
<p class="card-text abs" style="left:162px;top:1082px;width:177px">Sed ut perspiciatis unde omnis iste natus error sit voluptatem.</p>
<p class="card-text abs" style="left:360px;top:1082px;width:177px">Sed ut perspiciatis unde omnis iste natus error sit voluptatem.</p>
<p class="card-text abs" style="left:559px;top:1082px;width:177px">Sed ut perspiciatis unde omnis iste natus error sit voluptatem.</p>
<h4 class="card-title abs" style="left:162px;top:1277px">Finibus Bonorum</h4>
<h4 class="card-title abs" style="left:360px;top:1277px">Finibus Bonorum</h4>
<h4 class="card-title abs" style="left:559px;top:1277px">Finibus Bonorum</h4>
<p class="card-text abs" style="left:162px;top:1301px;width:177px">Sed ut perspiciatis unde omnis iste natus error sit voluptatem.</p>
<p class="card-text abs" style="left:360px;top:1301px;width:177px">Sed ut perspiciatis unde omnis iste natus error sit voluptatem.</p>
<p class="card-text abs" style="left:559px;top:1301px;width:177px">Sed ut perspiciatis unde omnis iste natus error sit voluptatem.</p>

<div class="thumb abs" style="left:768px;top:928px;width:270px;height:202px;background:radial-gradient(ellipse at 45% 50%,#7a4a3a,#1e1414 80%);display:flex;align-items:center;justify-content:center" role="img" aria-label="Speaker presenting on a dark stage, featured video">
  <span class="play" style="width:56px;height:56px"><svg width="18" height="20"><path d="M2 1 L17 10 L2 19Z" fill="#fff"/></svg></span></div>
<h3 class="abs" style="left:768px;top:1150px;width:270px;font-size:16px;line-height:26px;font-weight:700;color:var(--orange)">Sed ut perspiciatis unde omn nat ed ut perspiciatis un.</h3>
<p class="abs" style="left:768px;top:1218px;width:270px;font-size:11px;line-height:18px">Sed ut perspiciatis unde omnis istenatus er or sit voluptatem accusantium doloremque laudantium, totam rem aperiam, eaque ipsa quae ab illo inventore veritatis et quasi</p>
<span class="abs" style="left:768px;top:1326px;font-size:11.5px;font-weight:600;color:var(--orange)">11:59 | March 2014</span>

<section class="about">
  <h2 class="abs" style="left:162px;top:66px;font-size:24px;font-weight:700;color:var(--ink)">ABOUT ROSS VALDANE</h2>
  <p class="abs" style="left:162px;top:120px;width:590px;font-size:12.5px;line-height:22px">Sed ut perspiciatis unde omnis iste natus error sit voluptatem accusantium doloremque laudantium, totam rem aperiam, eaque ipsa quae ab one voluptatem.</p>
  <p class="abs" style="left:162px;top:186px;width:590px;font-size:10.5px;line-height:19px">Sed ut perspiciatis unde omnis iste natus error sit voluptatem accusantium doloremque laudantium, totam rem aperiam, eaque ipsa quae ab illo inventore veritatis et quasi architecto beatae vitae dicta sunt explicabo. Nemo enim ipsam voluptatem quia voluptas sit aspernatur aut odit aut fugit, sed quia consequuntur magni dolores eos qui ratione voluptatem sequi nesciunt. Neque porro quisquam est, qui dolorem ipsumenim ipsam voluptatem quia voluptas sit aspernatur aut odit aut fugit, sed quia consequuntur magni dolores eos qui ratione voluptatem sequi nesciunt. Neque porro quisquam est, qui dolorem ipsum.</p>
  <div class="btn-orange abs" style="left:162px;top:331px;width:103px;height:40px">READ MORE</div>
  <div class="btn-outline abs" style="left:276px;top:331px;width:170px;height:40px"><svg width="9" height="11"><path d="M1 1 L8 5.5 L1 10Z" fill="#333"/></svg>WATCH THE TRAILER</div>
  <span class="abs" style="left:462px;top:341px;width:24px;height:22px;background:#d6d6d6"></span>
  <span class="abs" style="left:493px;top:341px;width:24px;height:22px;background:#d6d6d6"></span>
  <span class="abs" style="left:524px;top:341px;width:24px;height:22px;background:#d6d6d6"></span>
  <svg class="abs" style="left:566px;top:326px" width="56" height="52" viewBox="0 0 56 52" aria-hidden="true">
    <path d="M4 20 L28 4 L52 20 V48 H4Z" fill="#e8e8e8" stroke="#888" stroke-width="2"/>
    <rect x="12" y="14" width="32" height="22" fill="#fff" stroke="#aaa"/>
    <path d="M4 20 L28 36 L52 20" fill="none" stroke="var(--orange)" stroke-width="3"/>
  </svg>
  <div class="abs" style="left:766px;top:39px;width:302px;height:411px;background:linear-gradient(180deg,#d9c3b3 0%,#2f3f5c 45%,#1f2d47 100%);border-radius:140px 140px 0 0" role="img" aria-label="Portrait of the speaker in a navy suit with arms crossed"></div>
</section>

<section class="testimonials" role="img" aria-label="Darkened audience backdrop">
  <h2 class="section-title abs" style="top:64px;color:var(--white)">TESTIMONIALS</h2>
  <svg class="abs" style="left:985px;top:68px" width="52" height="24" aria-hidden="true">
    <circle cx="11" cy="12" r="10" fill="none" stroke="#fff" stroke-width="1.5"/><path d="M13 7 L8 12 L13 17" fill="none" stroke="#fff" stroke-width="1.8"/>
    <circle cx="39" cy="12" r="10" fill="none" stroke="#777" stroke-width="1.5"/><path d="M37 7 L42 12 L37 17" fill="none" stroke="#777" stroke-width="1.8"/>
  </svg>
  <div class="abs" style="left:191px;top:135px;width:124px;height:124px;border-radius:50%;border:4px solid #fff;background:linear-gradient(135deg,#e8c9a8,#b88660)" role="img" aria-label="Client portrait"></div>
  <span class="abs" style="left:345px;top:135px;color:#fff;font-size:26px;font-weight:800">“</span>
  <span class="abs" style="left:918px;top:190px;color:#fff;font-size:26px;font-weight:800">”</span>
  <h5 class="abs" style="left:343px;top:231px;color:#fff;font-size:12px;font-weight:700">JHON SMITH, <span style="font-size:9.5px;font-weight:600;color:#ddd">CITY NAME, LOREM SIPMDIL</span></h5>
</section>
<p class="quote abs">&nbsp;&nbsp;&nbsp;&nbsp;Sed ut perspiciatis unde omnis iste natus error sit voluptatem accusantium doloremque laudantium, totam rem aperiam, eaque ipsa quae ab illo inventore veritatis et quasi architecto beatae vitae dicta sunt explicaboni mpsam voluptatem quia voluptas sit aspernatur aut odit aut fugit, sed quia consequuntur magni</p>

<section class="recent-blog" style="top:2210px;height:406px">
  <h2 class="section-title abs" style="top:25px">RECENT BLOG POSTS</h2>
</section>
<div class="abs" style="left:162px;top:2296px;width:205px;height:139px;background:linear-gradient(135deg,#c8cfd6,#6a5a50)" role="img" aria-label="Seminar room with audience facing a presenter"></div>
<div class="abs" style="left:385px;top:2296px;width:205px;height:139px;background:linear-gradient(135deg,#5d7fa6,#2b2a38)" role="img" aria-label="Presenter on stage in front of a blue screen"></div>
<div class="abs" style="left:608px;top:2296px;width:204px;height:139px;background:linear-gradient(135deg,#d8a884,#5b3a30)" role="img" aria-label="Audience members laughing in a hall"></div>
<div class="abs" style="left:833px;top:2296px;width:205px;height:139px;background:linear-gradient(135deg,#e6e6e0,#7d8a6e)" role="img" aria-label="Trainer beside a flip chart with a group"></div>

<h4 class="card-title abs" style="left:162px;top:2447px">Finibus Bonorum</h4>
<h4 class="card-title abs" style="left:385px;top:2447px">Finibus Bonorum</h4>
<h4 class="card-title abs" style="left:608px;top:2447px">Finibus Bonorum</h4>
<h4 class="card-title abs" style="left:833px;top:2447px">Finibus Bonorum</h4>
<p class="card-text abs" style="left:162px;top:2472px;width:205px">Sed ut perspiciatis unde omnis iste nats error sit voluptatemeloid ut perspiciatis un domnis ite natus errvoluptatem.</p>
<p class="card-text abs" style="left:385px;top:2472px;width:205px">Sed ut perspiciatis unde omnis iste nats error sit voluptatemeloid ut perspiciatis un domnis ite natus errvoluptatem.</p>
<p class="card-text abs" style="left:608px;top:2472px;width:205px">Sed ut perspiciatis unde omnis iste nats error sit voluptatemeloid ut perspiciatis un domnis ite natus errvoluptatem.</p>
<p class="card-text abs" style="left:833px;top:2472px;width:205px">Sed ut perspiciatis unde omnis iste nats error sit voluptatemeloid ut perspiciatis un domnis ite natus errvoluptatem.</p>
<div class="meta abs" style="left:162px;top:2544px"><span><svg width="11" height="11"><rect x="1" y="2" width="9" height="8" fill="none" stroke="#333"/><rect x="1" y="2" width="9" height="2.5" fill="#333"/></svg>Aug 05,2016</span><span><svg width="12" height="10"><ellipse cx="6" cy="4.5" rx="5.5" ry="4" fill="#333"/><path d="M3 7 L2 10 L6 8Z" fill="#333"/></svg>Comments</span></div>
<div class="meta abs" style="left:385px;top:2544px"><span><svg width="11" height="11"><rect x="1" y="2" width="9" height="8" fill="none" stroke="#333"/><rect x="1" y="2" width="9" height="2.5" fill="#333"/></svg>Aug 05,2016</span><span><svg width="12" height="10"><ellipse cx="6" cy="4.5" rx="5.5" ry="4" fill="#333"/><path d="M3 7 L2 10 L6 8Z" fill="#333"/></svg>Comments</span></div>
<div class="meta abs" style="left:608px;top:2544px"><span><svg width="11" height="11"><rect x="1" y="2" width="9" height="8" fill="none" stroke="#333"/><rect x="1" y="2" width="9" height="2.5" fill="#333"/></svg>Aug 05,2016</span><span><svg width="12" height="10"><ellipse cx="6" cy="4.5" rx="5.5" ry="4" fill="#333"/><path d="M3 7 L2 10 L6 8Z" fill="#333"/></svg>Comments</span></div>
<div class="meta abs" style="left:833px;top:2544px"><span><svg width="11" height="11"><rect x="1" y="2" width="9" height="8" fill="none" stroke="#333"/><rect x="1" y="2" width="9" height="2.5" fill="#333"/></svg>Aug 05,2016</span><span><svg width="12" height="10"><ellipse cx="6" cy="4.5" rx="5.5" ry="4" fill="#333"/><path d="M3 7 L2 10 L6 8Z" fill="#333"/></svg>Comments</span></div>

<section class="booking">
  <h2 class="section-title abs" style="top:30px;color:var(--white)">BOOKING FORM</h2>
  <svg class="abs" style="left:712px;top:18px" width="32" height="40" aria-hidden="true"><path d="M24 3 L29 8 L10 32 L4 35 L6 28Z" fill="none" stroke="#fff" stroke-width="2"/><path d="M21 7 L26 12" stroke="#fff" stroke-width="2"/></svg>
  <div class="field abs" style="left:172px;top:86px;width:285px;height:39px">Name:</div>
  <div class="field abs" style="left:172px;top:130px;width:285px;height:37px">Email:</div>
  <div class="field abs" style="left:172px;top:172px;width:285px;height:37px">Phone:</div>
  <div class="field select abs" style="left:467px;top:86px;width:280px;height:39px">Police:<svg width="9" height="6"><path d="M0 0 H9 L4.5 6Z" fill="#333"/></svg></div>
  <div class="field select abs" style="left:467px;top:130px;width:280px;height:37px">Date:<svg width="11" height="11"><rect x="0.5" y="1.5" width="10" height="9" fill="none" stroke="#333"/><rect x="0.5" y="1.5" width="10" height="3" fill="#333"/></svg></div>
  <div class="field select abs" style="left:467px;top:172px;width:280px;height:37px">Time:<svg width="9" height="6"><path d="M0 0 H9 L4.5 6Z" fill="#333"/></svg></div>
  <div class="field abs" style="left:757px;top:86px;width:269px;height:123px;align-items:flex-start;padding-top:10px">Message:</div>
  <div class="btn-dark abs" style="left:873px;top:213px;width:153px;height:40px">REQUEST HERE</div>
</section>

<section class="recent-presentations" style="top:2906px;height:344px">
  <h2 class="abs" style="left:160px;top:45px;font-size:24px;font-weight:700">RECENT PRESENTATIONS</h2>
  <h3 class="abs" style="left:162px;top:91px;font-size:15.5px;font-weight:700;color:var(--orange)">Sed ut perspiciatis unde omnis iste natus sit volu</h3>
  <p class="abs" style="left:162px;top:124px;width:440px;font-size:10.5px;line-height:19px">Sed ut perspiciatis unde omnis iste natus error sit voluptatem accusantium dolor emque laudantium, totam rem aperiam, eaque ipsa quae ab illo inventore veritatis et quasi architecto beatae vitae dicta sunt explicabo. mo enim ipsam voluptatlaudantium, totam rem aperiam, eaque ipsa quae ab illo inventore veritatis et quasi architecto beatae vitae dicta sunt exp.</p>
  <div class="meta abs" style="left:162px;top:224px"><span><svg width="11" height="11"><rect x="1" y="2" width="9" height="8" fill="none" stroke="#333"/><rect x="1" y="2" width="9" height="2.5" fill="#333"/></svg>Aug 05,2016</span><span><svg width="12" height="10"><ellipse cx="6" cy="4.5" rx="5.5" ry="4" fill="#333"/><path d="M3 7 L2 10 L6 8Z" fill="#333"/></svg>Comments</span></div>
  <div class="btn-orange abs" style="left:162px;top:255px;width:104px;height:36px">READ MORE</div>
  <div class="abs" style="left:648px;top:53px;width:390px;height:237px;background:radial-gradient(ellipse at 70% 70%,#d86c4a 0%,#4a4f66 45%,#1c2236 100%)" role="img" aria-label="Presenter at a laptop facing a large conference audience"></div>
</section>

<footer class="site-footer">
  <div class="brand abs" style="top:27px;color:var(--white);font-size:28px;line-height:28px">ROSS<br>VALDANE</div>
  <nav class="footer-nav" aria-label="Footer">
    <a style="left:408px;top:34px">HOME</a>
    <a style="left:464px;top:34px">MEET ROSS</a>
    <a style="left:546px;top:34px">BLOG</a>
    <a style="left:597px;top:34px">KEYNOTES &amp; SPEAKING</a>
    <a style="left:743px;top:34px">TRAINING &amp; WEBINARS</a>
    <a style="left:888px;top:34px">COACHING &amp; CONSULTING</a>
    <a style="left:408px;top:60px">TESTIMONIALS</a>
    <a style="left:510px;top:60px">BOOK ROSS</a>
    <a style="left:595px;top:60px">MEDIA INQUIRIES</a>
    <a style="left:720px;top:60px">CONTACT</a>
  </nav>
  <span class="abs" style="left:162px;top:107px;width:876px;height:1px;background:#4a4a4a"></span>
  <span class="abs" style="left:162px;top:136px;font-size:8.5px;font-weight:600;color:#aaa">KEEP IN TOUCH</span>
  <span class="social abs" style="left:162px;top:154px"></span>
  <span class="social abs" style="left:194px;top:154px"></span>
  <span class="social abs" style="left:226px;top:154px"></span>
  <span class="social abs" style="left:258px;top:154px;background:var(--orange)"></span>
  <div class="field abs" style="left:408px;top:139px;width:230px;height:37px;font-style:normal;color:#555">Name:</div>
  <div class="field abs" style="left:650px;top:139px;width:230px;height:37px;font-style:normal;color:#555">Email:</div>
  <div class="btn-orange abs" style="left:889px;top:139px;width:149px;height:37px">SUBSCRIBE HERE</div>
  <span class="abs" style="right:162px;top:195px;font-size:9px;color:#bbb">© 2016 Ross Valdane. All right reserved Term of Use</span>
</footer>

</body>
</html>
```